FR banner

we need a banner design (36"x120" horizontal) that will be displayed on a local high school baseball field. My company ( Crestwell Prints Co) has been producing signage for the Fernmoor Ridge community since 2009. We would like to communicate that we do more than banners. The final design should include the slogan "Signs Shirts Swag" and our Logo.

Target Market(s)

companies, teams, events, shirt and other marketing items.

Industry/Entity Type

Sign, Print,

Font styles to use
Sans Serif

Requirements
Should not have
• no baseball content.

```html
<!DOCTYPE html>
<html lang="en">
<head>
<meta charset="utf-8">
<title>Crestwell Prints Co — Field Banner</title>
<link href="https://fonts.googleapis.com/css2?family=Montserrat:wght@800;900&display=swap" rel="stylesheet">
<style>
  :root {
    --page: #e9ecf1;
    --cyan: #00aeef;
    --white: #ffffff;
    --ink: #0a0a0a;
    --purple-top: #2b3389;
    --purple-mid: #26115a;
    --purple-deep: #1a0a45;
    --accent-blue: #34589a;
  }
  * { margin: 0; padding: 0; box-sizing: border-box; }
  html, body {
    width: 1200px;
    height: 1178px;
    overflow: hidden;
    background: var(--page);
  }
  .banner {
    position: absolute;
    left: 0;
    top: 409px;
    width: 1200px;
    height: 360px;
    overflow: hidden;
  }
  .banner-shapes {
    position: absolute;
    inset: 0;
    display: block;
  }
  .brand-name {
    position: absolute;
    left: 34px;
    top: 118px;
    width: 330px;
    font-family: "Montserrat", sans-serif;
    font-weight: 900;
    font-size: 50px;
    line-height: 1.02;
    letter-spacing: -0.5px;
    color: var(--ink);
    text-transform: uppercase;
  }
  .slogan {
    position: absolute;
    left: 540px;
    top: 18px;
    width: 500px;
    text-align: center;
    font-family: "Montserrat", sans-serif;
    font-weight: 900;
    font-size: 110px;
    line-height: 94px;
    letter-spacing: -1px;
    text-transform: uppercase;
  }
  .slogan-line { display: block; color: var(--white); }
  .slogan-line--accent { color: var(--cyan); }
</style>
</head>
<body>
  <section class="banner" aria-label="Crestwell Prints Co field banner">
    <svg class="banner-shapes" width="1200" height="360" viewBox="0 0 1200 360" aria-hidden="true">
      <defs>
        <linearGradient id="purpleField" x1="0" y1="0" x2="0" y2="1">
          <stop offset="0" stop-color="#2b3389"/>
          <stop offset="0.45" stop-color="#26115a"/>
          <stop offset="1" stop-color="#1a0a45"/>
        </linearGradient>
      </defs>
      <rect class="brand-panel" x="0" y="0" width="1200" height="360" fill="var(--cyan)"/>
      <polygon class="divider-stripe" points="511,0 1200,0 1200,360 371,360" fill="var(--white)"/>
      <polygon class="slogan-panel" points="527,0 1200,0 1200,360 390,360" fill="url(#purpleField)"/>
      <polygon class="corner-accent-left" points="390,360 460,360 430,255" fill="var(--accent-blue)"/>
      <polygon class="corner-accent-right" points="1200,140 1200,360 1108,360" fill="var(--accent-blue)"/>
    </svg>

    <div class="brand-name">Crestwell Prints Co</div>

    <h1 class="slogan">
      <span class="slogan-line">Signs</span>
      <span class="slogan-line slogan-line--accent">Shirts</span>
      <span class="slogan-line">Swag</span>
    </h1>
  </section>
</body>
</html>
```